Business Book - Quiet Mornings at the Ledger Desk (Finding Calm Among Daily Numbers)

I'm looking for a cover that appeals to successful business people who are used to reading business titles.

The cover should feel familiar and fit in with the existing canon of bestselling business books with a vibrant, but professional look (see attached).

I want my book to stand out, but not to be frivolous. Abstract is probably best. Or close to it.

Please feel free to use my brand colours, or go with something else -

Teal
HEX #199BAB
25 / 155 / 171

Coral
HEX #EE786E
238 / 120/ 110

I don't want to include anything connected with robots or gendered assistants/business people. Or headsets.

It's only 24 hours which is mental

```html
<!DOCTYPE html>
<html lang="en">
<head>
<meta charset="utf-8">
<title>Quiet Mornings at the Ledger Desk — Book Cover</title>
<link rel="stylesheet" href="https://fonts.googleapis.com/css2?family=Montserrat:wght@200;300;800&family=Oswald:wght@500&family=Source+Serif+4:ital,wght@1,300&display=swap">
<style>
  :root {
    --page-bg: #c9c9c9;
    --cover-grey-light: #b4b4b4;
    --cover-grey-mid: #9d9d9d;
    --cover-grey-dark: #8a8a8a;
    --warm-tone: rgba(214, 170, 140, 0.45);
    --title-white: #ffffff;
    --coral: #e8675c;
  }

  * { margin: 0; padding: 0; box-sizing: border-box; }

  html, body {
    width: 1200px;
    height: 900px;
    overflow: hidden;
    background: var(--page-bg);
  }

  .stage {
    position: relative;
    width: 1200px;
    height: 900px;
  }

  .book-cover {
    position: absolute;
    left: 295px;
    top: 20px;
    width: 610px;
    height: 860px;
    overflow: hidden;
    color: var(--title-white);
  }

  .cover-photo {
    position: absolute;
    inset: 0;
    background:
      radial-gradient(ellipse 42% 48% at 50% 72%, var(--warm-tone), transparent 70%),
      linear-gradient(180deg, var(--cover-grey-mid) 0%, var(--cover-grey-light) 45%, var(--cover-grey-dark) 100%);
  }

  .title-line {
    position: absolute;
    left: 50px;
    font-family: "Montserrat", sans-serif;
    line-height: 1;
    white-space: nowrap;
  }

  .title-thin {
    top: 40px;
    font-size: 92px;
    font-weight: 200;
    letter-spacing: -3px;
  }

  .title-bold {
    top: 136px;
    font-size: 78px;
    font-weight: 800;
    letter-spacing: -2px;
  }

  .title-outline {
    font-size: 88px;
    font-weight: 300;
    letter-spacing: -3px;
    word-spacing: 18px;
    color: transparent;
    -webkit-text-stroke: 1.3px var(--title-white);
  }
  .title-outline.line-1 { top: 232px; }
  .title-outline.line-2 { top: 322px; }
  .title-outline.line-3 { top: 412px; }

  .subtitle-badge {
    position: absolute;
    left: 447px;
    top: 235px;
    width: 166px;
    height: 166px;
    border-radius: 50%;
    background: var(--coral);
    display: flex;
    align-items: center;
    justify-content: center;
    text-align: center;
    font-family: "Source Serif 4", serif;
    font-style: italic;
    font-weight: 300;
    font-size: 19px;
    line-height: 1.3;
  }

  .author-name {
    position: absolute;
    left: 0;
    right: 0;
    top: 794px;
    text-align: center;
    font-family: "Oswald", sans-serif;
    font-weight: 500;
    font-size: 27px;
    letter-spacing: 0.2px;
    line-height: 1;
  }
</style>
</head>
<body>
  <main class="stage">
    <section class="book-cover">
      <div class="cover-photo" role="img" aria-label="Cover photograph: softly lit studio portrait on a pale grey backdrop"></div>

      <h1 class="book-title">
        <span class="title-line title-thin">QUIET</span>
        <span class="title-line title-bold">MORNINGS</span>
        <span class="title-line title-outline line-1">AT THE</span>
        <span class="title-line title-outline line-2">LEDGER</span>
        <span class="title-line title-outline line-3">DESK</span>
      </h1>

      <p class="subtitle-badge">Finding Calm<br>Among<br>Daily<br>Numbers</p>

      <p class="author-name">NAME SURNAME</p>
    </section>
  </main>
</body>
</html>
```